Corvallin Property Solutions need a business card design

Hello guys. We would need a business card design asap please.
We are a start up property investment business based in London UK specialised in buying, selling, managing and letting properties and helping distressed property owners.
The name of our Business is Corvallin, the logo symbolises the four fundamental elements of the world (earth, air, fire and water) and so it stands for strength, stability, longevity.
We would like the business card to communicate professionalism and reliability. Many many thanks indeed for your work.

Details:

1.) Marisol Dunkley
Property Investor
Mobile: +44(0)7700362517
Email: marisol.corvallin@quilbrook.example

2.) Tomas Brindle
Property Investor
Mobile: +44(0)7700845926
Email: tomas.corvallin@quilbrook.example

Industry/Entity Type

Investment

```html
<!DOCTYPE html>
<html lang="en">
<head>
<meta charset="utf-8">
<title>Corvallin Property Solutions — Business Card</title>
<link rel="stylesheet" href="https://fonts.googleapis.com/css2?family=Open+Sans:wght@400;700&display=swap">
<style>
  :root {
    --page-bg: #d9d6d1;
    --card-black: #0b0b0b;
    --text-light: #e6e6e6;
    --text-muted: #bdbdbd;
    --accent-blue: #3d6fc4;
  }
  * { margin: 0; padding: 0; box-sizing: border-box; }
  html, body {
    width: 1200px;
    height: 1000px;
    overflow: hidden;
    background: var(--page-bg);
    font-family: "Open Sans", Arial, sans-serif;
  }
  .sheet {
    position: relative;
    width: 1200px;
    height: 1000px;
  }
  .card {
    position: absolute;
    left: 250px;
    width: 700px;
    height: 400px;
    background: var(--card-black);
    box-shadow: 0 10px 28px rgba(0,0,0,0.35);
  }
  .card--front { top: 70px; }
  .card--back { top: 530px; }

  .brand {
    position: absolute;
    display: flex;
    align-items: center;
    gap: 18px;
  }
  .brand__mark {
    width: 26px;
    height: 26px;
    background: var(--accent-blue);
  }
  .brand__name {
    color: var(--text-light);
    font-weight: 700;
    text-transform: uppercase;
    letter-spacing: 0.02em;
    line-height: 1;
  }
  .brand__tagline {
    color: var(--text-muted);
    font-weight: 700;
    text-transform: uppercase;
    letter-spacing: 0.02em;
  }

  .card--front .brand { left: 170px; top: 160px; }
  .card--front .brand__name { font-size: 50px; }
  .card--front .brand__tagline {
    position: absolute;
    left: 214px;
    top: 228px;
    font-size: 22px;
  }

  .card--back .brand { right: 60px; top: 56px; }
  .card--back .brand__name { font-size: 34px; }
  .card--back .brand__tagline {
    position: absolute;
    right: 60px;
    top: 104px;
    font-size: 15px;
  }

  .contact {
    position: absolute;
    left: 60px;
    top: 180px;
    color: var(--text-light);
  }
  .contact__name {
    font-size: 22px;
    font-weight: 700;
    text-transform: uppercase;
    letter-spacing: 0.01em;
  }
  .contact__role {
    font-size: 16px;
    color: var(--text-muted);
    margin-bottom: 14px;
  }
  .contact__line {
    font-size: 16px;
    line-height: 1.6;
  }
</style>
</head>
<body>
  <main class="sheet">
    <section class="card card--front" aria-label="Card front">
      <div class="brand">
        <span class="brand__mark"></span>
        <span class="brand__name">Corvallin</span>
      </div>
      <p class="brand__tagline">Property Solutions</p>
    </section>

    <section class="card card--back" aria-label="Card back">
      <div class="brand">
        <span class="brand__mark"></span>
        <span class="brand__name">Corvallin</span>
      </div>
      <p class="brand__tagline">Property Solutions</p>

      <div class="contact">
        <p class="contact__name">Marisol Dunkley</p>
        <p class="contact__role">Property Investor</p>
        <p class="contact__line">Mobile: +44(0)7700362517</p>
        <p class="contact__line">Email: marisol.corvallin@quilbrook.example</p>
      </div>
    </section>
  </main>
</body>
</html>
```